Funky physio needs a business card to match!

We are a physiotherapy clinic and pilates studio who specialise in sports and spinal injuries, as well as persistent or chronic pain.

We would like a vibrant and fun business card which is not over medicalised.

PO Box number is 418

Industry/Entity Type

Clinic

Contact Information for Business Card

Kestrel Sports Medicine
Suite 4 & 5 Wattlegrove Rd, BRACKENVALE VIC 3192
p 86203947
f 9614 3852
e admin@kestrelsportsmedicine.com.au
w kestrelsportsmedicine.com.au

All correspondence via email or mailed to:
PO Box
BRACKENVALE VIC 3192

Requirements
Must have
• Must have a green element - see logo. I don't mind if the business card is green, or if it's black, grey, white etc with green highlights. I'm the physio ... you're the designer!!!! It just needs to "look" green!
Our font is Harabara and can be downloaded from typelofts.com
Nice to have
• Please check our website to get a feel of our company. We don't take ourselves to seriously, however want to be taken seriously!
Should not have
• not over medicalised or corporate

```html
<!DOCTYPE html>
<html lang="en">
<head>
<meta charset="utf-8">
<title>Kestrel Sports Medicine Business Card</title>
<link rel="stylesheet" href="https://fonts.googleapis.com/css2?family=Ubuntu:wght@400;500;700&display=swap">
<style>
  :root {
    --stage: #6f6f6f;
    --white: #ffffff;
    --green-deep: #1f5a08;
    --green-mid: #3f8f10;
    --green-bright: #7cc61e;
    --lime: #a8e02a;
    --brand-green: #4c9a12;
    --text-light: #f3f8ec;
    --label: #ffffff;
  }
  * { box-sizing: border-box; margin: 0; padding: 0; }
  html, body {
    width: 1200px; height: 861px; overflow: hidden;
    background: var(--stage);
    font-family: "Ubuntu", Arial, sans-serif;
  }
  .stage {
    width: 1200px; height: 861px;
    display: flex; align-items: center; justify-content: center; gap: 50px;
  }
  .card {
    position: relative;
    width: 525px; height: 300px;
    border-radius: 6px;
    overflow: hidden;
    background: linear-gradient(160deg, var(--green-bright) 0%, var(--green-mid) 45%, var(--green-deep) 100%);
    box-shadow: 0 12px 30px rgba(0,0,0,0.35);
  }
  .card-header {
    position: absolute; inset: 0 0 auto 0; height: 300px;
  }
  .card-header svg { display: block; }
  .brand {
    position: absolute; top: 38px; left: 32px;
    display: flex; align-items: center; gap: 16px;
  }
  .brand-dot {
    width: 68px; height: 68px; border-radius: 50%;
    border: 6px solid var(--brand-green);
  }
  .brand-name {
    font-weight: 500; font-size: 30px; color: var(--brand-green);
    white-space: nowrap; letter-spacing: 0.2px;
  }
  .about {
    position: absolute; left: 30px; right: 30px; top: 150px;
    color: var(--text-light); text-align: center;
    font-size: 15px; line-height: 1.3;
  }
  .about p + p { margin-top: 16px; }
  .about strong { font-weight: 700; }
  .contact {
    position: absolute; left: 34px; right: 20px; top: 140px;
    display: grid; grid-template-columns: 92px 1fr; row-gap: 4px;
    color: var(--text-light); font-size: 14px; line-height: 1.25;
  }
  .contact dt { font-weight: 700; font-size: 12px; color: var(--label); letter-spacing: 0.5px; padding-top: 2px; }
</style>
</head>
<body>
<main class="stage">

  <section class="card card-about" aria-label="Business card, about side">
    <div class="card-header">
      <svg width="525" height="300" viewBox="0 0 525 300" aria-hidden="true">
        <path d="M0 0 H525 V108 H200 Q190 108 186 118 L182 128 Q178 138 168 138 H12 Q0 138 0 126 Z" fill="var(--white)"/>
        <path d="M186 110 Q192 112 200 112 H525 V120 H204 Q194 120 190 128 L186 136 Q182 146 168 146 H0 V138 H168 Q178 138 182 128 Z" fill="var(--lime)"/>
      </svg>
    </div>
    <div class="brand">
      <span class="brand-dot"></span>
      <span class="brand-name">Kestrel Sports Medicine</span>
    </div>
    <div class="about">
      <p><strong>Kestrel Sports Medicine</strong> provides quality services for all types of injuries – sporting and everyday injuries.</p>
      <p><strong>Kestrel Sports Medicine</strong> is now also providing Pilates services, and will soon introduce Mums and Bubs classes for new mothers!</p>
    </div>
  </section>

  <section class="card card-contact" aria-label="Business card, contact side">
    <div class="card-header">
      <svg width="525" height="300" viewBox="0 0 525 300" aria-hidden="true">
        <path d="M0 0 H525 V108 H200 Q190 108 186 118 L182 128 Q178 138 168 138 H12 Q0 138 0 126 Z" fill="var(--white)"/>
        <path d="M186 110 Q192 112 200 112 H525 V120 H204 Q194 120 190 128 L186 136 Q182 146 168 146 H0 V138 H168 Q178 138 182 128 Z" fill="var(--lime)"/>
      </svg>
    </div>
    <div class="brand">
      <span class="brand-dot"></span>
      <span class="brand-name">Kestrel Sports Medicine</span>
    </div>
    <dl class="contact">
      <dt>ADDRESS</dt><dd>Kestrel Sports Medicine Suite 4 &amp; 5 Wattlegrove Rd, Brackenvale VIC 3192</dd>
      <dt>PHONE</dt><dd>86203947</dd>
      <dt>FAX</dt><dd>9614 3852</dd>
      <dt>E-MAIL</dt><dd>admin@kestrelsportsmedicine.com.au</dd>
      <dt>WEBSITE</dt><dd>kestrelsportsmedicine.com.au</dd>
      <dt>ALL MAIL</dt><dd>PO Box 418 Brackenvale VIC 3192</dd>
    </dl>
  </section>

</main>
</body>
</html>
```